Business Card Design Project

Hi!
Looking for a business card design for my acupuncture/remedial massage business using a logo I've just had designed through this site!
I'd like the following details included:
Logo (obviously)
My name - Miranda Pellowtane
Clinic details -Complementary and Traditional Chinese Medicine Haven
42 Brindlewood Road
Ashbury Heights 3152
03 9471 6820
Website - www.pellowtanewell.com.au
I have the logo design in two different colour combinations, one predominantly green, and the other in reverse colours. I was thinking that the green logo would take up one whole side of the business card, then we could include the reverse logo on the more detailed side. I'd like to see how that looks.
I also had the idea that the heart in the logo could be printed in metallic red (depending on cost). Not sure if that comes into play now or at the printers.
Thanks!

```html
<!DOCTYPE html>
<html lang="en">
<head>
<meta charset="utf-8">
<title>Pellowtane Well – Business Card</title>
<link rel="stylesheet" href="https://fonts.googleapis.com/css2?family=Share+Tech+Mono&display=swap">
<style>
  :root {
    --green: #1fae88;
    --red: #e2202b;
    --white: #ffffff;
    --ink: #3d8f78;
    --stage: #5b5b5b;
    --mono: "Share Tech Mono", monospace;
  }
  * { box-sizing: border-box; margin: 0; padding: 0; }
  html, body { width: 1200px; height: 672px; overflow: hidden; }
  body {
    background: var(--stage);
    font-family: var(--mono);
    position: relative;
  }
  .card {
    position: absolute;
    top: 186px;
    width: 525px;
    height: 300px;
    overflow: hidden;
  }
  .card--front {
    left: 50px;
    background: var(--green);
    border-radius: 48px 10px 48px 10px;
  }
  .card--back {
    left: 625px;
    background: var(--white);
    border-radius: 10px 48px 10px 48px;
  }

  /* Brand name (shared) */
  .brand {
    display: flex;
    align-items: center;
    gap: 14px;
    color: var(--white);
    white-space: nowrap;
  }
  .brand__dot {
    width: 22px; height: 22px;
    border-radius: 50%;
    background: var(--red);
    flex: none;
  }
  .brand__name { font-size: 40px; line-height: 1; }
  .card--front .brand {
    position: absolute;
    left: 60px; top: 122px;
  }

  /* Back */
  .card--back .brand {
    position: absolute;
    left: 26px; top: 96px;
    color: var(--green);
    gap: 8px;
  }
  .card--back .brand__dot { width: 12px; height: 12px; }
  .card--back .brand__name { font-size: 20px; }

  .name-tab {
    position: absolute;
    right: 0; top: 34px;
    width: 300px; height: 34px;
    background: var(--green);
    border-radius: 17px 0 0 17px;
    color: var(--white);
    font-size: 18px;
    line-height: 34px;
    padding-left: 26px;
    white-space: nowrap;
  }
  .clinic {
    position: absolute;
    right: 26px; top: 128px;
    text-align: right;
    color: var(--red);
    font-size: 15px;
    line-height: 1.3;
    white-space: nowrap;
  }
  .address {
    position: absolute;
    right: 26px; top: 178px;
    text-align: right;
    color: var(--ink);
    font-size: 13px;
    line-height: 1.35;
    white-space: nowrap;
  }
  .web-band {
    position: absolute;
    left: 0; right: 0; bottom: 0;
    height: 46px;
    background: var(--green);
    color: var(--white);
    font-size: 15px;
    text-align: center;
    line-height: 40px;
    letter-spacing: 1px;
  }
</style>
</head>
<body>
  <section class="card card--front" aria-label="Card front">
    <div class="brand">
      <span class="brand__dot"></span>
      <span class="brand__name">Pellowtane Well</span>
    </div>
  </section>

  <section class="card card--back" aria-label="Card back">
    <div class="brand">
      <span class="brand__dot"></span>
      <span class="brand__name">Pellowtane Well</span>
    </div>
    <div class="name-tab">Miranda Pellowtane</div>
    <p class="clinic">Complementary &amp; Traditional<br>Chinese Medicine Haven</p>
    <p class="address">42 Brindlewood Road<br>Ashbury Heights 3152<br>PHONE : 03 9471 6820</p>
    <div class="web-band">www.pellowtanewell.com.au</div>
  </section>
</body>
</html>
```